Business Consulting Business Card

professional business card with basic information (1) First and Last name (2) email address, (3) phone number, (4) website.

```html
<!DOCTYPE html>
<html lang="en">
<head>
<meta charset="utf-8">
<title>Coral Pine Capital Realty — Business Card</title>
<link rel="stylesheet" href="https://fonts.googleapis.com/css2?family=Montserrat:wght@400;500;600;700&family=Poppins:wght@400;500&display=swap">
<style>
  :root {
    --stage: #1a1b1d;
    --card: #232628;
    --ink: #f2f4f5;
    --teal: #4fbcc8;
    --teal-deep: #2e9fb0;
    --muted: #c9d0d3;
  }
  * { box-sizing: border-box; margin: 0; padding: 0; }
  html, body {
    width: 1200px; height: 800px; overflow: hidden;
    background: var(--stage);
  }
  .stage {
    position: relative; width: 1200px; height: 800px;
    display: flex; align-items: center; justify-content: center; gap: 40px;
  }
  .card {
    position: relative; width: 540px; height: 309px;
    background: var(--card);
    overflow: hidden;
    box-shadow: 0 14px 30px rgba(0,0,0,.45);
  }
  .card__band {
    position: absolute; left: 0; right: 0; bottom: 0; height: 10px;
    background: var(--teal);
  }

  /* Front */
  .front__brand {
    position: absolute; inset: 0 0 10px 0;
    display: flex; flex-direction: column; align-items: center; justify-content: center;
  }
  .brand__mark {
    width: 46px; height: 46px; border-radius: 50%;
    background: linear-gradient(135deg, var(--teal), var(--teal-deep));
    margin-bottom: 18px;
  }
  .brand__name {
    font-family: "Montserrat", sans-serif; font-weight: 500;
    font-size: 38px; letter-spacing: 9px; color: var(--ink);
    padding-left: 9px;
  }
  .brand__tagline {
    margin-top: 10px;
    font-family: "Montserrat", sans-serif; font-weight: 500;
    font-size: 12px; letter-spacing: 5px; color: var(--teal);
    padding-left: 5px;
  }

  /* Back */
  .back__wordmark {
    position: absolute; top: 44px; right: 40px;
    font-family: "Montserrat", sans-serif; font-weight: 500;
    font-size: 28px; letter-spacing: 7px; color: var(--ink);
  }
  .back__mark {
    position: absolute; top: 104px; left: 40px;
    width: 44px; height: 44px; border-radius: 50%;
    background: linear-gradient(135deg, var(--teal), var(--teal-deep));
  }
  .person { position: absolute; top: 164px; left: 40px; }
  .person__name {
    font-family: "Montserrat", sans-serif; font-weight: 700;
    font-size: 20px; letter-spacing: 1.5px; color: var(--ink);
  }
  .person__title {
    font-family: "Poppins", sans-serif; font-weight: 400;
    font-size: 15px; color: var(--teal); margin-top: -2px;
  }
  .contact {
    position: absolute; left: 40px; top: 218px;
    list-style: none; display: grid; gap: 4px;
  }
  .contact__item {
    display: flex; align-items: center; gap: 9px;
    font-family: "Poppins", sans-serif; font-size: 12.5px; color: var(--muted);
    line-height: 16px;
  }
  .contact__icon { width: 16px; height: 16px; flex: none; }
</style>
</head>
<body>
<main class="stage">

  <section class="card card--front" aria-label="Business card front">
    <div class="front__brand">
      <span class="brand__mark" aria-hidden="true"></span>
      <span class="brand__name">CORAL PINE</span>
      <span class="brand__tagline">CAPITAL | REALTY</span>
    </div>
    <div class="card__band"></div>
  </section>

  <section class="card card--back" aria-label="Business card back">
    <div class="back__wordmark">CORAL PINE</div>
    <span class="back__mark" aria-hidden="true"></span>
    <div class="person">
      <div class="person__name">LEO NAVARRO</div>
      <div class="person__title">Principal</div>
    </div>
    <ul class="contact">
      <li class="contact__item">
        <svg class="contact__icon" viewBox="0 0 16 16" aria-hidden="true">
          <circle cx="8" cy="8" r="8" fill="var(--teal)"/>
          <rect x="5.5" y="3.5" width="5" height="9" rx="1" fill="none" stroke="#232628" stroke-width="1.3"/>
        </svg>
        305.555.0147
      </li>
      <li class="contact__item">
        <svg class="contact__icon" viewBox="0 0 16 16" aria-hidden="true">
          <circle cx="8" cy="8" r="8" fill="var(--teal)"/>
          <rect x="4" y="5" width="8" height="6" fill="none" stroke="#232628" stroke-width="1.2"/>
          <path d="M4 5 L8 8.5 L12 5" fill="none" stroke="#232628" stroke-width="1.2"/>
        </svg>
        lnavarro@coralpine.com
      </li>
      <li class="contact__item">
        <svg class="contact__icon" viewBox="0 0 16 16" aria-hidden="true">
          <circle cx="8" cy="8" r="8" fill="var(--teal)"/>
          <circle cx="8" cy="8" r="4.2" fill="none" stroke="#232628" stroke-width="1.1"/>
          <ellipse cx="8" cy="8" rx="1.8" ry="4.2" fill="none" stroke="#232628" stroke-width="1"/>
          <line x1="3.8" y1="8" x2="12.2" y2="8" stroke="#232628" stroke-width="1"/>
        </svg>
        www.coralpinecapital.com
      </li>
      <li class="contact__item">
        <svg class="contact__icon" viewBox="0 0 16 16" aria-hidden="true">
          <circle cx="8" cy="8" r="8" fill="var(--teal)"/>
          <circle cx="8" cy="8" r="4.2" fill="none" stroke="#232628" stroke-width="1.1"/>
          <ellipse cx="8" cy="8" rx="1.8" ry="4.2" fill="none" stroke="#232628" stroke-width="1"/>
          <line x1="3.8" y1="8" x2="12.2" y2="8" stroke="#232628" stroke-width="1"/>
        </svg>
        www.coralpine.com
      </li>
    </ul>
    <div class="card__band"></div>
  </section>

</main>
</body>
</html>
```